I need the following on my business card:
- Name: Dana Whitcomb
- License # 0M93216
- Title: Producer
- Phone: (555) 017-3904
- Email: Dana@CorbelInsuranceServices.com

- Company: Corbel Insurance Services
- Address: 27408 Larkmoor Ave Suite 610, Fairhaven Ridge, CA 90217
- Website: www.CorbelInsuranceServices.com

Also add our slogan on the card: "Steady Advice, Honest Cover"

```html
<!DOCTYPE html>
<html lang="en">
<head>
<meta charset="utf-8">
<title>Corbel Insurance Services — Business Card</title>
<link href="https://fonts.googleapis.com/css2?family=Open+Sans:wght@400;600;700;800&display=swap" rel="stylesheet">
<style>
  :root {
    --navy: #1f2a6b;
    --green: #0b9444;
    --ink: #1a1a1a;
    --paper: #f7f7f6;
    --backdrop: #e4e2df;
  }
  * { margin: 0; padding: 0; box-sizing: border-box; }
  html, body {
    width: 1200px; height: 997px; overflow: hidden;
    background: var(--backdrop);
    font-family: "Open Sans", Arial, sans-serif;
  }
  .canvas { position: relative; width: 1200px; height: 997px; }
  .card {
    position: absolute;
    width: 525px; height: 300px;
    box-shadow: 0 6px 18px rgba(0,0,0,0.12);
    overflow: hidden;
  }
  /* Back side */
  .card-back {
    left: 80px; top: 190px;
    background: var(--navy);
    display: flex; flex-direction: column; align-items: center; justify-content: center;
    color: #fff;
  }
  .brand-name {
    font-weight: 700;
    letter-spacing: 0.12em;
    text-transform: uppercase;
    text-align: center;
    line-height: 1.25;
  }
  .card-back .brand-name { font-size: 26px; color: #fff; }
  .card-back .website { margin-top: 40px; font-size: 15px; font-weight: 600; letter-spacing: 0.01em; }

  /* Front side */
  .card-front { left: 595px; top: 520px; background: var(--paper); }
  .base-band {
    position: absolute; left: 0; right: 0; bottom: 0; height: 78px;
    background: var(--navy);
    border-top: 10px solid var(--green);
  }
  .contact {
    position: absolute; right: 26px; top: 20px;
    text-align: right; color: var(--ink);
  }
  .card-front .brand-name { font-size: 19px; color: var(--navy); margin-bottom: 10px; }
  .person { font-size: 16px; font-weight: 800; }
  .person .title { color: var(--green); }
  .license { font-size: 11.5px; font-weight: 700; margin-top: 2px; }
  .details { font-size: 11.5px; line-height: 1.4; margin-top: 6px; }
  .details .label { color: var(--green); }
  .address { font-size: 11.5px; line-height: 1.4; margin-top: 3px; }
  .slogan {
    position: absolute; left: 28px; bottom: 14px;
    color: #fff; font-weight: 700; font-size: 16px; line-height: 1.2;
  }
</style>
</head>
<body>
<div class="canvas">

  <section class="card card-back">
    <div class="brand-name">Corbel<br>Insurance Services</div>
    <div class="website">CorbelInsuranceServices.com</div>
  </section>

  <section class="card card-front">
    <div class="base-band"></div>
    <div class="contact">
      <div class="brand-name">Corbel<br>Insurance Services</div>
      <div class="person">Dana Whitcomb | <span class="title">Producer</span></div>
      <div class="license">License # 0M93216</div>
      <div class="details">
        <div><span class="label">Phone:</span> (555) 017-3904</div>
        <div>Dana@CorbelInsuranceServices.com</div>
      </div>
      <div class="address">
        <div>Corbel Insurance Services</div>
        <div>27408 Larkmoor Ave Suite 610</div>
        <div>Fairhaven Ridge, CA 90217</div>
      </div>
    </div>
    <div class="slogan">Steady Advice,<br>Honest Cover</div>
  </section>

</div>
</body>
</html>
```